Velmora Interiors Stationary Set

Velmora Interiors is a bespoke interior design firm set to provide services to VIP clients with elegance and minimalism is the main theme for our stationary set. We require a full stationary set covering A4 letterhead, A4 & A3 envelopes, business cards, USB's, CDs, email signature and any other item the designer sees fit. logo is already designed and finalized, and we require the designer to use it as is without modifying the logo.

Address to be used on letterhead / business cards ...etc shall be as follows:

Phone : +971 2 518 3074
P.O. Box : 609318
Address: Block C&D, Bldg. 27, Court 14, Abu Dhabi, United Arab Emirates
Website: www.velmorainteriors-example.com

Target Market(s)

VIP Clients

Industry/Entity Type

Interior Design

Other font styles liked:
• something to be unique

Colors

Designer to choose colors to be used in the design.

Requirements
Must have
• Elegant, minimalistic
Nice to have
• Simple yet elegant design having a sharp yet clean cut format
Should not have
• No additional colours, just colours that are used in the logo (silver, black or gold)

```html
<!DOCTYPE html>
<html lang="en">
<head>
<meta charset="utf-8">
<title>Velmora Interiors – Stationery Set</title>
<link rel="stylesheet" href="https://fonts.googleapis.com/css2?family=Jost:wght@300;400;500;600&display=swap">
<style>
  :root{
    --bg:#8c8c8c;
    --paper:#f7f7f7;
    --white:#ffffff;
    --gold:#c4a467;
    --ink:#1d1d1d;
    --charcoal:#3a3a3a;
    --graphite:#565656;
    --silver:#d8d8d8;
    --text:#4a4a4a;
    --muted:#7a7a7a;
  }
  *{box-sizing:border-box;margin:0;padding:0}
  html,body{width:1200px;height:872px;overflow:hidden}
  body{
    background:radial-gradient(ellipse at 50% 40%,#a3a3a3 0%,var(--bg) 70%,#7c7c7c 100%);
    font-family:"Jost",sans-serif;color:var(--text);position:relative;
  }
  .item{position:absolute;overflow:hidden;background:linear-gradient(160deg,var(--white),var(--paper) 60%,#ececec);box-shadow:0 4px 10px rgba(0,0,0,.35)}
  .item.bare{background:none;box-shadow:none;overflow:visible;filter:drop-shadow(0 4px 6px rgba(0,0,0,.35))}
  .item > svg.cut{position:absolute;inset:0;width:100%;height:100%}
  .brand{position:absolute;color:var(--gold);font-weight:300;line-height:1;white-space:nowrap}
  .brand .name{display:block;letter-spacing:.04em}
  .brand .sub{display:block;letter-spacing:.32em;margin-top:.35em;font-size:.38em}
  .contact{position:absolute;list-style:none;color:var(--text);font-weight:400}
  .contact li{display:flex;align-items:flex-start;gap:.7em;margin-bottom:.45em;line-height:1.25;white-space:nowrap}
  .contact svg{width:1em;height:1em;flex:none;fill:var(--graphite);margin-top:.1em}

  /* email signature */
  .signature{left:45px;top:44px;width:373px;height:68px}
  .signature .brand{left:18px;top:15px;font-size:18px}
  .signature .contact{left:97px;top:19px;font-size:4.6px}
  .signature .contact li{margin-bottom:.3em}
  .social{position:absolute;left:109px;top:53px;display:flex;gap:2px}
  .social span{width:4px;height:4px;border-radius:50%;background:var(--graphite)}

  /* letterhead */
  .letterhead{left:45px;top:226px;width:296px;height:395px}
  .letterhead .header{position:absolute;left:0;top:0;width:100%;height:112px;background:linear-gradient(180deg,#ffffff,#ececec)}
  .letterhead .brand{left:42px;top:52px;font-size:24px}
  .letterhead .contact{left:196px;top:46px;font-size:6px}
  .letterhead .headline{position:absolute;left:37px;top:144px;font-size:12.5px;font-weight:300;letter-spacing:.04em;color:var(--charcoal)}
  .letterhead .body{position:absolute;left:37px;top:163px;width:229px;font-size:5.4px;line-height:1.38;text-align:justify;color:var(--muted)}
  .letterhead .body p{margin-bottom:6px}
  .letterhead .sign{position:absolute;right:32px;top:323px;text-align:right;font-size:5.8px;line-height:1.35;color:var(--charcoal)}
  .letterhead .sign .role{font-weight:600;color:var(--muted)}
  .letterhead .sign .line{font-weight:500}

  /* notebook */
  .notebook{left:453px;top:42px;width:222px;height:297px;background:linear-gradient(160deg,#2b2b2b,#151515)}
  .notebook .brand{left:38px;top:32px;font-size:22px}

  /* business cards */
  .card{width:143px;height:82px}
  .card-front{left:370px;top:423px}
  .card-front .brand{left:19px;top:27px;font-size:13px}
  .card-back{left:370px;top:527px}
  .card-back .brand{left:16px;top:30px;font-size:12px}
  .card-back .divider{position:absolute;left:68px;top:18px;width:.5px;height:50px;background:var(--silver)}
  .card-back .person{position:absolute;left:76px;top:29px;font-size:5.6px;font-weight:500;color:var(--ink);letter-spacing:.02em}
  .card-back .person small{display:block;font-size:2.8px;font-weight:500;color:var(--muted);margin-top:1px}
  .card-back .contact{left:76px;top:42px;font-size:3.2px}
  .card-back .contact li{margin-bottom:.3em}

  /* CD */
  .disc{position:absolute;left:637px;top:426px;width:180px;height:180px;border-radius:50%;overflow:hidden;box-shadow:0 4px 10px rgba(0,0,0,.35);background:linear-gradient(160deg,#fff,#efefef)}
  .disc svg{position:absolute;inset:0;width:100%;height:100%}
  .sleeve{left:541px;top:421px;width:188px;height:188px}
  .sleeve .brand{left:28px;top:22px;font-size:19px}
  .hub{position:absolute;left:705px;top:494px;width:44px;height:44px;border-radius:50%;background:radial-gradient(circle,#8a8a8a 0 45%,#cfcfcf 47% 100%);box-shadow:0 1px 3px rgba(0,0,0,.3)}

  /* DL envelope front & back */
  .envelope-front{left:42px;top:677px;width:305px;height:158px}
  .envelope-front .brand{left:23px;top:17px;font-size:19px}
  .envelope-front .window{position:absolute;left:145px;top:77px;width:132px;height:57px;border-radius:4px;background:linear-gradient(180deg,#e4e4e4,#cfcfcf);box-shadow:inset 0 0 0 1px #c4c4c4}
  .envelope-front .contact{left:17px;top:100px;font-size:3.9px}
  .envelope-front .contact li{margin-bottom:.3em}
  .envelope-back{left:372px;top:635px;width:304px;height:200px}
  .envelope-back svg,.envelope-large svg{position:absolute;inset:0;width:100%;height:100%}

  /* ID card */
  .id-card{left:706px;top:754px;width:134px;height:82px;background:linear-gradient(180deg,#f4f4f4,#e8e8e8)}
  .id-card .photo{position:absolute;left:13px;top:24px;width:40px;height:40px;border-radius:50%;background:radial-gradient(circle at 50% 40%,#b8b8b8,#8a8a8a)}
  .id-card .person{position:absolute;left:62px;top:28px;font-size:4.6px;font-weight:500;color:var(--ink)}
  .id-card .person small{display:block;font-size:2.4px;color:var(--muted);margin-top:1px}
  .id-card .contact{left:62px;top:39px;font-size:2.7px}
  .id-card .contact li{margin-bottom:.3em}
  .id-card .hole{position:absolute;top:6px;width:4px;height:4px;border-radius:50%;background:#9a9a9a}

  /* A3 envelope */
  .envelope-large{left:868px;top:430px;width:294px;height:406px}
  .envelope-large .brand{right:16px;bottom:12px;font-size:24px}
</style>
</head>
<body>

<svg width="0" height="0" style="position:absolute" aria-hidden="true">
  <defs>
    <linearGradient id="dark" x1="0" y1="0" x2="1" y2="1">
      <stop offset="0" stop-color="#6a6a6a"/><stop offset=".55" stop-color="#3c3c3c"/><stop offset="1" stop-color="#1c1c1c"/>
    </linearGradient>
    <linearGradient id="flap" x1="0" y1="0" x2="0" y2="1">
      <stop offset="0" stop-color="#3e3e3e"/><stop offset="1" stop-color="#141414"/>
    </linearGradient>
    <linearGradient id="body" x1="0" y1="0" x2="0" y2="1">
      <stop offset="0" stop-color="#f0f0f0"/><stop offset="1" stop-color="#ffffff"/>
    </linearGradient>
    <linearGradient id="gold" x1="0" y1="1" x2="1" y2="0">
      <stop offset="0" stop-color="#b89756"/><stop offset=".5" stop-color="#d2b57c"/><stop offset="1" stop-color="#b39252"/>
    </linearGradient>
    <symbol id="ic-web" viewBox="0 0 16 16"><path d="M8 1a7 7 0 1 0 0 14A7 7 0 0 0 8 1zm0 2c1 1.2 1.6 3 1.7 5H6.3C6.4 6 7 4.2 8 3zM3.1 9h2.2c.1 1.6.5 3 1.1 4A5 5 0 0 1 3.1 9zm0-2a5 5 0 0 1 3.3-4c-.6 1-1 2.4-1.1 4zm4.9 6c-1-1.2-1.6-2.4-1.7-4h3.4c-.1 1.6-.7 2.8-1.7 4zm1.6 0c.6-1 1-2.4 1.1-4h2.2a5 5 0 0 1-3.3 4zm1.1-6c-.1-1.6-.5-3-1.1-4a5 5 0 0 1 3.3 4z"/></symbol>
    <symbol id="ic-pin" viewBox="0 0 16 16"><path d="M8 1a5 5 0 0 0-5 5c0 3.8 5 9 5 9s5-5.2 5-9a5 5 0 0 0-5-5zm0 7a2 2 0 1 1 0-4 2 2 0 0 1 0 4z"/></symbol>
    <symbol id="ic-mail" viewBox="0 0 16 16"><path d="M1 4h14v9H1zm1.5 1.2L8 9l5.5-3.8V5h-11z"/></symbol>
    <symbol id="ic-phone" viewBox="0 0 16 16"><path d="M4.2 1.5 6.5 4 5.2 5.8a9 9 0 0 0 5 5l1.8-1.3 2.5 2.3-1.6 2.2C7.5 14 2 8.5 2 3z"/></symbol>
  </defs>
</svg>

<!-- Email signature -->
<section class="item signature" aria-label="Email signature">
  <svg class="cut" viewBox="0 0 100 100" preserveAspectRatio="none">
    <polygon points="46,100 100,0 100,3 51,100" fill="#dcdcdc"/>
    <polygon points="51,100 100,3 100,32 73,100" fill="url(#gold)"/>
    <polygon points="73,100 100,32 100,100" fill="url(#dark)"/>
  </svg>
  <div class="brand"><span class="name">Velmora</span><span class="sub">INTERIORS</span></div>
  <ul class="contact">
    <li><svg><use href="#ic-web"/></svg>www.velmorainteriors-example.com</li>
    <li><svg><use href="#ic-pin"/></svg>Block C&amp;D, Bldg. 27, Court 14,<br>Abu Dhabi, United Arab Emirates</li>
    <li><svg><use href="#ic-mail"/></svg>609318</li>
    <li><svg><use href="#ic-phone"/></svg>+971 2 518 3074</li>
  </ul>
  <div class="social" aria-hidden="true"><span></span><span></span><span></span><span></span><span></span><span></span><span></span><span></span></div>
</section>

<!-- Notebook cover -->
<section class="item notebook" aria-label="Notebook cover">
  <svg class="cut" viewBox="0 0 100 100" preserveAspectRatio="none">
    <polygon points="0,83 100,53 100,56 0,86" fill="#4a4a4a"/>
    <polygon points="0,86 100,56 100,66 0,94" fill="url(#gold)"/>
    <polygon points="0,94 100,66 100,100 0,100" fill="url(#dark)"/>
  </svg>
  <div class="brand"><span class="name">Velmora</span><span class="sub">INTERIORS</span></div>
</section>

<!-- Letterhead -->
<section class="item letterhead" aria-label="A4 letterhead">
  <div class="header"></div>
  <svg class="cut" viewBox="0 0 100 100" preserveAspectRatio="none">
    <polygon points="0,0 40,0 0,10" fill="url(#dark)"/>
    <polygon points="0,10 40,0 55,0 0,16" fill="url(#gold)"/>
    <polygon points="0,16 55,0 58,0 0,17" fill="#ffffff"/>
    <polygon points="44,100 100,83 100,85 50,100" fill="#dcdcdc"/>
    <polygon points="50,100 100,85 100,93 76,100" fill="url(#gold)"/>
    <polygon points="76,100 100,93 100,100" fill="url(#dark)"/>
  </svg>
  <div class="brand"><span class="name">Velmora</span><span class="sub">INTERIORS</span></div>
  <ul class="contact">
    <li><svg><use href="#ic-web"/></svg>www.velmorainteriors-example.com</li>
    <li><svg><use href="#ic-pin"/></svg>Block C&amp;D, Bldg. 27, Court 14,<br>Abu Dhabi, United Arab Emirates</li>
    <li><svg><use href="#ic-mail"/></svg>609318</li>
    <li><svg><use href="#ic-phone"/></svg>+971 2 518 3074</li>
  </ul>
  <h1 class="headline">SUBJECT HEADLINE HERE</h1>
  <div class="body">
    <p>Classic business stationery, i.e., letterheads, business cards, and envelopes, is just as important as e-mails when it comes to corporate design. All these forms of business communication end up in the hands of many different people. Here, too, we ensure visual homogeneity by using a standard form of design.</p>
    <p>We are completely consistent across all forms of customer contact. Visual coherence also governs other elements of business communication. These range from supposedly “minor details”, such as file spines and visitor badges, to frequently used Word and Excel templates. To make work easier, templates for all elements of business communication can be downloaded. These are binding and comply not only with our corporate design guidelines, but also with valid DIN standards, as well as postal and legal requirements.</p>
  </div>
  <div class="sign">
    <div class="role">Creative Art Director</div>
    <div class="line">Pellentesque id neque ligula. Nullam posuere</div>
    <div>www.velmorainteriors-example.com</div>
  </div>
</section>

<!-- Business card front -->
<section class="item card card-front" aria-label="Business card front">
  <svg class="cut" viewBox="0 0 100 100" preserveAspectRatio="none">
    <polygon points="0,76 100,30 100,33 0,80" fill="#dcdcdc"/>
    <polygon points="0,80 100,33 100,50 0,95" fill="url(#gold)"/>
    <polygon points="0,95 100,50 100,100 0,100" fill="url(#dark)"/>
  </svg>
  <div class="brand"><span class="name">Velmora</span><span class="sub">INTERIORS</span></div>
</section>

<!-- Business card back -->
<section class="item card card-back" aria-label="Business card back">
  <svg class="cut" viewBox="0 0 100 100" preserveAspectRatio="none">
    <polygon points="0,0 20,0 0,12" fill="url(#dark)"/>
    <polygon points="0,12 20,0 45,0 0,30" fill="url(#gold)"/>
    <polygon points="0,30 45,0 48,0 0,32" fill="#ffffff"/>
    <polygon points="44,100 100,62 100,65 48,100" fill="#dcdcdc"/>
    <polygon points="48,100 100,65 100,80 74,100" fill="url(#gold)"/>
    <polygon points="74,100 100,80 100,100" fill="url(#dark)"/>
  </svg>
  <div class="brand"><span class="name">Velmora</span><span class="sub">INTERIORS</span></div>
  <div class="divider"></div>
  <div class="person">KARIM NASSER<small>CO-FOUNDER BUSINESS NAME</small></div>
  <ul class="contact">
    <li><svg><use href="#ic-web"/></svg>www.velmorainteriors-example.com</li>
    <li><svg><use href="#ic-pin"/></svg>Block C&amp;D, Bldg. 27, Court 14,<br>Abu Dhabi, United Arab Emirates</li>
    <li><svg><use href="#ic-mail"/></svg>609318</li>
    <li><svg><use href="#ic-phone"/></svg>+971 2 518 3074</li>
  </ul>
</section>

<!-- CD label and sleeve -->
<div class="disc" aria-label="CD label">
  <svg viewBox="0 0 100 100" preserveAspectRatio="none">
    <polygon points="0,50 100,40 100,43 0,53" fill="#dcdcdc"/>
    <polygon points="0,53 100,43 100,56 0,70" fill="url(#gold)"/>
    <polygon points="0,70 100,56 100,100 0,100" fill="url(#dark)"/>
  </svg>
</div>
<section class="item sleeve" aria-label="CD sleeve">
  <svg class="cut" viewBox="0 0 100 100" preserveAspectRatio="none">
    <polygon points="0,63 100,28 100,31 0,66" fill="#dcdcdc"/>
    <polygon points="0,66 100,31 100,45 0,88" fill="url(#gold)"/>
    <polygon points="0,88 100,45 100,100 0,100" fill="url(#dark)"/>
  </svg>
  <div class="brand"><span class="name">Velmora</span><span class="sub">INTERIORS</span></div>
</section>
<div class="hub" aria-hidden="true"></div>

<!-- DL envelope front -->
<section class="item envelope-front" aria-label="DL envelope front">
  <svg class="cut" viewBox="0 0 100 100" preserveAspectRatio="none">
    <polygon points="0,86 100,18 100,24 0,92" fill="#dcdcdc"/>
    <polygon points="0,92 100,24 100,47 31,100 0,100" fill="url(#gold)"/>
    <polygon points="31,100 100,47 100,100" fill="url(#dark)"/>
  </svg>
  <div class="brand"><span class="name">Velmora</span><span class="sub">INTERIORS</span></div>
  <div class="window"></div>
  <ul class="contact">
    <li><svg><use href="#ic-web"/></svg>www.velmorainteriors-example.com</li>
    <li><svg><use href="#ic-pin"/></svg>Block C&amp;D, Bldg. 27, Court 14,<br>Abu Dhabi, United Arab Emirates</li>
    <li><svg><use href="#ic-mail"/></svg>609318</li>
    <li><svg><use href="#ic-phone"/></svg>+971 2 518 3074</li>
  </ul>
</section>

<!-- DL envelope back -->
<section class="item bare envelope-back" aria-label="DL envelope back">
  <svg viewBox="0 0 304 200" preserveAspectRatio="none">
    <rect x="0" y="42" width="304" height="158" fill="url(#body)"/>
    <path d="M22 0H282Q296 0 299 12L304 42H0L5 12Q8 0 22 0Z" fill="url(#flap)"/>
    <path d="M0 42H304L283 78Q278 88 264 88H40Q26 88 21 78Z" fill="url(#flap)"/>
    <rect x="0" y="42" width="304" height="10" fill="#0e0e0e"/>
  </svg>
</section>

<!-- ID card -->
<section class="item id-card" aria-label="Staff ID card">
  <svg class="cut" viewBox="0 0 100 100" preserveAspectRatio="none">
    <polygon points="34,100 100,62 100,65 38,100" fill="#dcdcdc"/>
    <polygon points="38,100 100,65 100,78 58,100" fill="url(#gold)"/>
    <polygon points="58,100 100,78 100,100" fill="url(#dark)"/>
  </svg>
  <span class="hole" style="left:34px"></span><span class="hole" style="left:96px"></span>
  <div class="photo" role="img" aria-label="Staff portrait photo placeholder"></div>
  <div class="person">KARIM NASSER<small>CO-FOUNDER BUSINESS NAME</small></div>
  <ul class="contact">
    <li><svg><use href="#ic-web"/></svg>www.velmorainteriors-example.com</li>
    <li><svg><use href="#ic-pin"/></svg>Block C&amp;D, Bldg. 27, Court 14,<br>Abu Dhabi, United Arab Emirates</li>
    <li><svg><use href="#ic-mail"/></svg>609318</li>
    <li><svg><use href="#ic-phone"/></svg>+971 2 518 3074</li>
  </ul>
</section>

<!-- A3 envelope -->
<section class="item bare envelope-large" aria-label="A3 envelope">
  <svg viewBox="0 0 294 406" preserveAspectRatio="none">
    <rect x="0" y="41" width="294" height="365" fill="url(#body)"/>
    <polygon points="0,318 294,224 294,231 0,326" fill="#dcdcdc"/>
    <polygon points="0,326 294,231 294,264 0,364" fill="url(#gold)"/>
    <polygon points="0,364 294,264 294,406 0,406" fill="url(#dark)"/>
    <path d="M26 0H268Q282 0 286 12L294 41H0L8 12Q12 0 26 0Z" fill="url(#flap)"/>
    <path d="M0 41H294L280 72Q275 83 262 83H32Q19 83 14 72Z" fill="url(#flap)"/>
    <rect x="0" y="41" width="294" height="9" fill="#0e0e0e"/>
  </svg>
  <div class="brand"><span class="name">Velmora</span><span class="sub">INTERIORS</span></div>
</section>

</body>
</html>
```